Hearth & Keg Room requires web site design - Casual restaurant

Need website designed for re-branding of Restaurant based in Fort Morgan, Colorado. We offer a wide variety of American cuisine in a casual, rustic atmosphere. We're offering 16 craft beers on draft, as well as a full service bar, and modern, interesting menu selections in a friendly, fun and energetic environment, with an emphasis on superior customer service and high quality, locally sourced food. We are a family, and community service oriented establishment. The website design should convey a welcoming sense, "simplicity", yet sophisticated - without pretentiousness. The website should effectively convey our "home style" relaxed atmosphere, as well as our casual character.

Business Hours: Sunday - Thursday, 11am-10pm / Friday & Saturday, 11am-11am

The Dunlo Hearth & Keg Room
2736 Pennick Road
Fort Morgan, Colorado 80701
B: (970) 555-0173

WEBSITE ADDRESS: thedunlokegroom.com

Target Market(s)

Young Adults
Families
Blue and White Collar Americans
Senior Citizens
Small town location, appeal to everyone

Industry/Entity Type

American Restaurant

Contact Information for Business Card

Marcus T Ellery
Food & Beverage Director
2736 Pennick Road
B: (970) 555-0173
M: (231) 555-0148
mtellery@dunlokegroom.com
www.thedunlokegroom.com
***Use logo in uploaded files
***Open to single OR double sided
*** I will have additional names and information to add to this, for other employees.

Coding

Coded - Design and coding required

Number of Pages Required

5+ page

Font styles to use
Serif
Sans Serif
Decorative
Other font styles liked:
• Calafornian FB,

Requirements
Must have
• Home/Welcome Page
• Menu Page/Online Ordering Ready
• About Us/Contact Us page
• Catering/Private Events/Banquets Advertising section
• Ability to link to Facebook/TripAdvisor/Yelp/Instagram etc.
• Logo uploaded, reference for colors as well.
Nice to have
• About craft beer page
• Our Story/Bio section
• Photo Gallery
• Employment/Apply section
Should not have
• We are NOT a "fine dining" restaurant... think casual...

```html
<!DOCTYPE html>
<html lang="en">
<head>
<meta charset="utf-8">
<title>The Dunlo Hearth &amp; Keg Room</title>
<link rel="stylesheet" href="https://fonts.googleapis.com/css2?family=Oswald:wght@400;500&family=Roboto:wght@400;500;700&family=Alegreya:wght@400;700&display=swap">
<style>
:root{
  --orange:#e8560f;
  --orange-dark:#c9470a;
  --ink:#222;
  --grey-bg:#efefef;
  --text:#555;
  --footer:#1e2630;
  --footer-line:#3a4450;
  --white:#fff;
}
*{box-sizing:border-box;margin:0;padding:0}
html,body{width:1200px;height:4276px;overflow:hidden}
body{position:relative;font-family:"Roboto",sans-serif;color:var(--ink);background:var(--white)}
.abs{position:absolute}
.serif{font-family:"Alegreya",serif}
.cond{font-family:"Oswald",sans-serif}

/* hero */
.hero{left:0;top:0;width:1200px;height:641px;background:radial-gradient(ellipse at 50% 40%,#7a5a43 0%,#4a3426 45%,#22170f 100%)}
.hero-brand{left:463px;top:91px;width:276px;height:276px;border-radius:50%;background:var(--white);display:flex;align-items:center;justify-content:center}
.hero-brand span{font-family:"Alegreya",serif;font-weight:700;font-size:44px;color:var(--ink)}
.hero-tag{left:0;width:1200px;top:426px;text-align:center;font-family:"Oswald",sans-serif;font-size:33px;color:var(--white);letter-spacing:.5px}
.hero-addr{left:0;width:1200px;top:472px;text-align:center;font-family:"Oswald",sans-serif;font-size:19px;color:var(--white);letter-spacing:1px}
.hero-phone{left:0;width:1200px;top:500px;text-align:center;font-family:"Oswald",sans-serif;font-size:34px;color:var(--orange)}

/* nav */
.nav{left:0;top:641px;width:1200px;height:57px;background:var(--white);display:flex;align-items:center;font-family:"Alegreya",serif;font-size:15px;letter-spacing:.5px}
.nav a{position:absolute;color:var(--ink);text-decoration:none}
.nav a.is-active{color:var(--orange)}

/* welcome */
.welcome{left:0;top:698px;width:1200px;height:456px;background:var(--grey-bg)}
.welcome-card{left:162px;top:57px;width:451px;height:351px;background:var(--orange);padding:56px 34px 0 38px;color:var(--white)}
.welcome-card h2{font-family:"Alegreya",serif;font-size:30px;font-weight:400;letter-spacing:.5px}
.welcome-card h3{font-family:"Alegreya",serif;font-size:19px;font-weight:400;margin-bottom:22px}
.welcome-card p{font-size:11.5px;line-height:1.55;width:360px;margin-bottom:8px}
.btn-light{display:inline-block;background:var(--white);color:var(--ink);font-size:11px;font-weight:700;padding:7px 12px;margin-top:12px}
.welcome-photo{left:570px;top:100px;width:547px;height:265px;background:linear-gradient(135deg,#3a1d0c,#8a4a1c 45%,#2a1208)}

/* menu banner */
.menu-banner{left:0;top:1154px;width:1200px;height:385px;background:radial-gradient(ellipse at 60% 45%,#b9862e 0%,#6a4418 45%,#2a1a0c 100%)}
.banner-title{left:0;width:1200px;top:140px;text-align:center;font-family:"Alegreya",serif;font-size:44px;color:var(--white);letter-spacing:2px}
.banner-sub{left:0;width:1200px;top:200px;text-align:center;font-family:"Alegreya",serif;font-size:20px;color:var(--white)}
.banner-rule{top:177px;height:1px;width:200px;background:rgba(255,255,255,.8)}

/* menu card */
.menu-section{left:0;top:1539px;width:1200px;height:670px;background:var(--white)}
.menu-card{left:100px;top:86px;width:840px;height:478px;background:var(--white);box-shadow:0 2px 10px rgba(0,0,0,.18)}
.menu-photo-left{left:0;top:0;width:170px;height:478px;background:linear-gradient(180deg,#f4efe8,#c4581e 40%,#8c3a12 70%,#eee)}
.menu-col{top:22px;width:300px}
.menu-col h3{font-family:"Alegreya",serif;font-size:36px;font-weight:400;color:var(--ink);border-bottom:3px solid var(--orange);padding-bottom:6px;margin-bottom:10px}
.menu-cat{display:flex;justify-content:space-between;align-items:baseline;font-family:"Alegreya",serif;color:var(--orange);font-size:17px;border-bottom:1px solid var(--orange);margin-top:9px}
.menu-cat .price{font-size:26px}
.menu-item{font-size:12px;font-weight:500;margin-top:6px}
.menu-desc{font-size:10.5px;color:var(--text);line-height:1.5}
.menu-divider{left:500px;top:22px;width:1px;height:440px;background:#ddd}
.menu-scroll{left:808px;top:36px;width:6px;height:420px;background:#eee}
.menu-scroll i{position:absolute;left:0;top:130px;width:6px;height:95px;background:var(--orange)}
.menu-photo-right{left:918px;top:1631px;width:165px;height:472px;background:linear-gradient(180deg,#2a2a2a,#6a6a6a 50%,#1e1e1e)}
.bowl-top{left:935px;top:1522px;width:265px;height:130px;border-radius:50%;background:radial-gradient(circle,#c9863e,#f4ede3 70%)}
.bowl-bottom{left:455px;top:2094px;width:215px;height:100px;border-radius:0 0 110px 110px;background:radial-gradient(circle at 50% 20%,#e08a2a,#f2ece4 70%)}

/* story */
.story{left:0;top:2209px;width:1200px;height:584px;background:var(--white)}
.story-title{left:0;width:1200px;top:92px;text-align:center;font-family:"Alegreya",serif;font-size:44px;color:var(--orange);letter-spacing:1px}
.story-sub{left:0;width:1200px;top:146px;text-align:center;font-family:"Alegreya",serif;font-size:20px}
.story-rule{top:124px;height:1px;width:190px;background:var(--orange)}
.chef-photo{left:162px;top:228px;width:237px;height:237px;border-radius:50%;border:6px solid var(--orange);background:linear-gradient(180deg,#f5f5f5,#dcdcdc)}
.chef-title{left:447px;top:262px;font-family:"Alegreya",serif;font-size:30px;font-weight:700}
.chef-title span{color:var(--orange)}
.story-text{top:322px;width:275px;font-size:11.5px;line-height:1.55;color:var(--text)}

/* gallery */
.gallery-band{left:0;top:2793px;width:1200px;height:100px;background:var(--orange)}
.gallery-band h2{position:absolute;left:0;width:1200px;top:28px;text-align:center;font-family:"Alegreya",serif;font-weight:400;font-size:38px;color:var(--white)}
.gallery{left:0;top:2893px;width:1200px;height:513px;background:linear-gradient(90deg,#d8d2ca,#eae6e0 50%,#cfc8bf)}
.g-tile{position:absolute;background:#555}
.dots{left:556px;top:3359px;display:flex;gap:8px}
.dots i{width:10px;height:10px;border-radius:50%;background:var(--ink)}
.dots i.on{background:var(--orange)}

/* contact */
.contact{left:0;top:3406px;width:1200px;height:442px;background:#e6e6e6}
.map{left:0;top:0;width:1200px;height:442px;background:linear-gradient(160deg,#ececec,#dedede)}
.contact-box{left:162px;top:34px;width:408px;height:399px;background:#f4f4f4}
.contact-photo{left:0;top:0;width:408px;height:150px;background:linear-gradient(90deg,#1d1410,#6b4a2c 50%,#1d1410)}
.contact-box h2{position:absolute;left:0;width:408px;top:168px;text-align:center;font-family:"Alegreya",serif;font-weight:700;font-size:32px;color:var(--orange)}
.field{position:absolute;left:20px;width:286px;height:30px;background:var(--white);border:1px solid #ddd;font-size:12px;padding:7px 10px;color:#444}
.btn-dark{position:absolute;left:110px;top:366px;background:#111;color:var(--white);font-size:13px;font-weight:500;padding:8px 14px}
.map-line{position:absolute;background:#fff}

/* footer */
.footer{left:0;top:3848px;width:1200px;height:370px;background:var(--footer);color:#cfd4da}
.info-box{top:34px;height:74px;border:1px solid var(--footer-line);display:flex;align-items:center;gap:14px;padding:0 14px;font-size:12px}
.info-icon{flex:none;width:40px;height:40px;background:var(--orange);display:flex;align-items:center;justify-content:center}
.info-box strong{font-family:"Alegreya",serif;color:var(--orange);font-weight:700;font-size:15px;display:block}
.f-head{top:140px;font-size:16px;font-weight:500;color:var(--white);letter-spacing:.5px}
.f-about{left:162px;top:172px;width:330px;font-size:11.5px;line-height:1.55}
.f-more{color:var(--orange);font-size:11px;display:block;margin-top:6px}
.socials{left:162px;top:298px;display:flex;gap:8px}
.socials i{width:24px;height:24px;border-radius:50%;border:1px solid #8a939c}
.f-links{left:576px;top:170px;list-style:none;font-size:12px;line-height:26px}
.f-links li::before{content:"› ";}
.news-input{left:826px;top:172px;width:200px;height:36px;background:#d9d9d9;color:#777;font-size:11px;padding:11px 10px}
.news-btn{left:826px;top:222px;background:var(--orange);color:var(--white);font-size:11px;font-weight:700;padding:8px 12px}
.copyright{left:0;top:4218px;width:1200px;height:58px;background:var(--orange);color:var(--white);text-align:center;font-size:11px;line-height:58px}
</style>
</head>
<body>

<section class="abs hero" role="img" aria-label="Photo of a busy dining room with guests at set tables">
  <div class="abs hero-brand"><span>The Dunlo</span></div>
  <div class="abs hero-tag">ONLY USING THE FINEST INGREDIENTS</div>
  <div class="abs hero-addr">2736 PENNICK ROAD, FORT MORGAN, COLORADO</div>
  <div class="abs hero-phone">(970) 555-0173</div>
</section>
<svg class="abs" style="left:580px;top:623px" width="40" height="20" viewBox="0 0 40 20"><path d="M0 20 L20 0 L40 20 Z" fill="#fff"/></svg>

<nav class="abs nav">
  <a class="is-active" style="left:213px">HOME</a>
  <a style="left:372px">MENU</a>
  <a style="left:532px">ABOUT US</a>
  <a style="left:722px">EVENTS</a>
  <a style="left:893px">CONTACT US</a>
</nav>

<section class="abs welcome">
  <div class="abs welcome-card">
    <h2>WELCOME TO THE DUNLO</h2>
    <h3>Hearth &amp; Keg Room</h3>
    <p>Lorem Ipsum is simply dummy text of the printing and typesetting industry. Lorem Ipsum has been the industry's standard dummy text ever since the 1500s, when an unknown printer took a galley of type and scrambled it to make a type specimen book. It has survived not only five centuries.</p>
    <p>Lorem Ipsum is simply dummy text of the printing and typesetting industry. Lorem Ipsum has been the industry's.</p>
    <span class="btn-light">READ MORE</span>
  </div>
  <div class="abs welcome-photo" role="img" aria-label="Photo of wine bottles lined up in front of a rack"></div>
</section>

<section class="abs menu-banner" role="img" aria-label="Photo of a glass of draft beer on a bar">
  <div class="abs banner-rule" style="left:330px"></div>
  <div class="abs banner-rule" style="left:670px"></div>
  <div class="abs banner-title">MENU</div>
  <div class="abs banner-sub">Hearth &amp; Keg Room</div>
</section>
<svg class="abs" style="left:560px;top:1524px" width="80" height="30" viewBox="0 0 80 30"><path d="M0 15 Q30 15 40 0 Q50 15 80 15 L80 30 L0 30 Z" fill="#fff"/></svg>

<section class="abs menu-section">
  <div class="abs menu-card">
    <div class="abs menu-photo-left" role="img" aria-label="Photo of glazed chicken wings"></div>
    <div class="abs menu-col" style="left:184px">
      <h3>LUNCH:</h3>
      <div class="menu-cat"><span>APPETIZERS</span><span class="price">$8.99</span></div>
      <div class="menu-item">QUESO LOADED FRITES</div>
      <div class="menu-desc">Crispy fries / bacon / pico de gallo queso sauce / chipotle</div>
      <div class="menu-cat"><span>FRESH GREENS</span><span class="price">$9.99</span></div>
      <div class="menu-item">CALIFORNIA WEDGE</div>
      <div class="menu-desc">Hickory bacon / heirloom tomato hass avocado / red onion hardboiled egg / romaine hearts bleu cheese dressing</div>
      <div class="menu-cat"><span>CRAFTWICHES</span><span class="price">$11.99</span></div>
      <div class="menu-item">CHICKEN CLUB</div>
      <div class="menu-desc">Lemon &amp; herb marinated grilled chicken breast hickory smoked bacon / monterey jack cheese mixed greens / tomato / toasted brioche / avocado cream</div>
      <div class="menu-cat"><span>HANDCRAFTED BURGERS</span></div>
      <div class="menu-item">JALAPEÑO</div>
      <div class="menu-desc">lettuce / tomato / grilled jalapeño / pepper jack crispy fried onions / sriracha buffalo sauce</div>
    </div>
    <div class="abs menu-divider"></div>
    <div class="abs menu-col" style="left:512px;width:286px">
      <h3>DINNER:</h3>
      <div class="menu-cat"><span>APPETIZERS</span><span class="price">$8.99</span></div>
      <div class="menu-item">QUESO LOADED FRITES</div>
      <div class="menu-desc">Crispy fries / bacon / pico de gallo queso sauce / chipotle</div>
      <div class="menu-cat"><span>FRESH GREENS</span><span class="price">$9.99</span></div>
      <div class="menu-item">CALIFORNIA WEDGE</div>
      <div class="menu-desc">Hickory bacon / heirloom tomato hass avocado / red onion hardboiled egg / romaine hearts bleu cheese dressing</div>
      <div class="menu-cat"><span>HAND TOSSED PIZZA</span><span class="price">$11.99</span></div>
      <div class="menu-item">THE BUTTE</div>
      <div class="menu-desc">pepperoni / italian sausage / onion / mushroom / bell pepper / mozzarella</div>
      <div class="menu-cat"><span>HANDCRAFTED BURGERS</span><span class="price">$11.99</span></div>
      <div class="menu-item">JALAPEÑO</div>
      <div class="menu-desc">lettuce / tomato / grilled jalapeño / pepper jack crispy fried onions / sriracha buffalo sauce</div>
    </div>
    <div class="abs menu-scroll"><i></i></div>
  </div>
</section>
<div class="abs bowl-top" role="img" aria-label="Photo of a bowl of baked onion soup"></div>
<div class="abs menu-photo-right" role="img" aria-label="Photo of a chef plating food in the kitchen"></div>
<div class="abs bowl-bottom" role="img" aria-label="Photo of a bowl of soup seen from above"></div>

<section class="abs story">
  <div class="abs story-rule" style="left:272px"></div>
  <div class="abs story-rule" style="left:738px"></div>
  <div class="abs story-title">OUR STORY</div>
  <div class="abs story-sub">Hearth &amp; Keg Room</div>
  <div class="abs chef-photo" role="img" aria-label="Photo of the head chef in whites"></div>
  <div class="abs chef-title">THE SUSHI CHEF: <span>Daniel Roark</span></div>
  <p class="abs story-text" style="left:447px">Lorem Ipsum is simply dummy text of the printing and typesetting industry. Lorem Ipsum has been the industry's standard dummy text ever since the 1500s, when an unknown printer took a galley of type and scrambled it to make a type specimen book. It has survived not only five centuries, but also the leap into electronic typesetting, remaining essentially unchanged. It was popularised in the 1960s with the release...</p>
  <p class="abs story-text" style="left:735px">Lorem Ipsum is simply dummy text of the printing and typesetting industry. Lorem Ipsum has been the industry's standard dummy text ever since the 1500s, when an unknown printer took a galley of type and scrambled it to make a type specimen book. It has survived not only five centuries, but also the leap into electronic typesetting, remaining essentially unchanged. It was popularised in the 1960s with the release...</p>
</section>

<section class="abs gallery-band"><h2>Photo Gallery</h2></section>
<svg class="abs" style="left:570px;top:2780px" width="60" height="14" viewBox="0 0 60 14"><path d="M0 14 L30 0 L60 14 Z" fill="#e8560f"/></svg>
<section class="abs gallery" role="img" aria-label="Photo gallery of dishes: salads, drinks, desserts and a sliced steak plate">
  <div class="g-tile" style="left:162px;top:48px;width:172px;height:128px;background:linear-gradient(135deg,#3b4a24,#6b7a3a)"></div>
  <div class="g-tile" style="left:162px;top:180px;width:172px;height:100px;background:linear-gradient(135deg,#5a3a1c,#b8843a)"></div>
  <div class="g-tile" style="left:162px;top:284px;width:172px;height:102px;background:linear-gradient(135deg,#4a2e1a,#8c5a30)"></div>
  <div class="g-tile" style="left:338px;top:48px;width:178px;height:224px;background:linear-gradient(180deg,#2a1e16,#c89238)"></div>
  <div class="g-tile" style="left:338px;top:276px;width:178px;height:110px;background:linear-gradient(135deg,#6a3a1c,#c8843a)"></div>
  <div class="g-tile" style="left:522px;top:48px;width:518px;height:338px;background:radial-gradient(ellipse at 55% 55%,#6a2a1a,#e8e4dc 60%)"></div>
</section>
<div class="abs dots"><i></i><i class="on"></i><i></i><i></i></div>

<section class="abs contact">
  <div class="abs map" role="img" aria-label="Street map of Fort Morgan with a pin on 2736 Pennick Road"></div>
  <svg class="abs" style="left:663px;top:198px" width="22" height="32" viewBox="0 0 22 32"><path d="M11 0 C4 0 0 5 0 11 C0 19 11 32 11 32 C11 32 22 19 22 11 C22 5 18 0 11 0 Z" fill="#e0332a"/><circle cx="11" cy="11" r="4" fill="#fff"/></svg>
  <div class="abs contact-box">
    <div class="abs contact-photo" role="img" aria-label="Photo of wine glasses on a bar counter"></div>
    <h2>Contact Now!</h2>
    <div class="field" style="top:218px">Name</div>
    <div class="field" style="top:258px">Phone Number</div>
    <div class="field" style="top:298px">Email</div>
    <span class="btn-dark">Submit Now!</span>
  </div>
</section>
<svg class="abs" style="left:570px;top:3834px" width="60" height="16" viewBox="0 0 60 16"><path d="M0 16 L30 0 L60 16 Z" fill="#1e2630"/></svg>

<footer class="abs footer">
  <div class="abs info-box" style="left:162px;width:240px">
    <span class="info-icon"><svg width="18" height="24" viewBox="0 0 22 32"><path d="M11 0 C4 0 0 5 0 11 C0 19 11 32 11 32 C11 32 22 19 22 11 C22 5 18 0 11 0 Z" fill="none" stroke="#fff" stroke-width="2.5"/><circle cx="11" cy="11" r="4" fill="#fff"/></svg></span>
    <div><strong>The Dunlo Hearth &amp; Keg Room</strong>2736 Pennick Road Fort Morgan, Colorado 80701</div>
  </div>
  <div class="abs info-box" style="left:464px;width:270px">
    <span class="info-icon"><svg width="20" height="20" viewBox="0 0 24 24"><path d="M6 2 L10 7 L8 10 C9 13 11 15 14 16 L17 14 L22 18 L19 22 C10 21 3 14 2 5 Z" fill="none" stroke="#fff" stroke-width="2"/></svg></span>
    <div style="font-family:'Alegreya',serif;font-size:17px"><span style="color:var(--orange)">Phone:</span> (970) 555-0173</div>
  </div>
  <div class="abs info-box" style="left:763px;width:277px">
    <span class="info-icon"><svg width="22" height="22" viewBox="0 0 24 24"><circle cx="12" cy="12" r="9" fill="none" stroke="#fff" stroke-width="2"/><path d="M12 7 V12 L15 14" stroke="#fff" stroke-width="2" fill="none"/></svg></span>
    <div><strong>Business Hours:</strong>Sunday - Thursday, 11am-10pm<br>Friday &amp; Saturday, 11am-11am</div>
  </div>
  <div class="abs f-head" style="left:162px">ABOUT US</div>
  <p class="abs f-about">Lorem Ipsum is simply dummy text of the printing and typesetting industry. Lorem Ipsum has been the industry's standard dummy text ever since the 1500s, when an unknown printer took a galley of type and scrambled it to make a type specimen book.<span class="f-more">Read More ›</span></p>
  <div class="abs socials"><i></i><i></i><i></i><i></i></div>
  <div class="abs f-head" style="left:566px">INFORMATION</div>
  <ul class="abs f-links"><li>Home</li><li>Menu</li><li>About Us</li><li>Events</li><li>Contacts</li></ul>
  <div class="abs f-head" style="left:826px">NEWSLETTER</div>
  <div class="abs news-input">Enter Your Email id</div>
  <div class="abs news-btn">SUBSCRIBE</div>
</footer>
<div class="abs copyright">Copyright 2017. All Right Reserved.</div>

</body>
</html>
```